Banner for fencing on construction sites

Banner to market our company on construction job sites Included on banner we would need something along the lines "Temp Labor" and our website "WWW.KRVLT.COM" all Visible enough to see as people are driving by.
The attached .ai file we provided has two images, we prefer the 2nd one with just VLT.
The Banner will be 7ft wide x 4ft height.

Target Market(s)

Construction Companies

Requirements
Must have
• Visible Website to drivers passing by
• VLT Logo has to be BIGGER than anything

```html
<!DOCTYPE html>
<html lang="en">
<head>
<meta charset="utf-8">
<title>VLT Temp Labor – Site Fencing Banner</title>
<link rel="stylesheet" href="https://fonts.googleapis.com/css2?family=Anton&family=Oswald:wght@600&display=swap">
<style>
  :root {
    --stage: #6b6b6b;
    --ink: #000000;
    --white: #ffffff;
    --orange-deep: #f07a2a;
    --orange-warm: #f5a23c;
    --sky-glow: #fbe3b0;
    --steel-amber: #b9742f;
  }
  html, body {
    margin: 0;
    width: 1200px;
    height: 1200px;
    overflow: hidden;
    background: var(--stage);
  }
  .banner {
    position: absolute;
    left: 176px;
    width: 848px;
    height: 484px;
    display: block;
  }
  .banner--deep { top: 74px; --accent: var(--orange-deep); }
  .banner--warm { top: 643px; --accent: var(--orange-warm); }
  .brand-name {
    font-family: "Anton", "Oswald", sans-serif;
    fill: var(--accent);
  }
  .site-url {
    font-family: "Anton", "Oswald", sans-serif;
    fill: var(--white);
  }
  .site-url .accent { fill: var(--accent); }
  .service-line {
    font-family: "Oswald", "Anton", sans-serif;
    font-weight: 600;
    fill: var(--accent);
  }
</style>
</head>
<body>

<svg class="banner banner--deep" viewBox="0 0 848 484" aria-label="VLT temp labor banner, deep orange version">
  <defs>
    <linearGradient id="photo-fade-a" x1="0" y1="0" x2="0" y2="1">
      <stop offset="0" stop-color="var(--steel-amber)" stop-opacity="0"/>
      <stop offset="0.55" stop-color="#3a2410" stop-opacity="0.6"/>
      <stop offset="0.82" stop-color="#000" stop-opacity="1"/>
    </linearGradient>
    <linearGradient id="photo-tone-a" x1="0" y1="0" x2="1" y2="0">
      <stop offset="0" stop-color="#a8652a"/>
      <stop offset="0.55" stop-color="#c98a45"/>
      <stop offset="1" stop-color="var(--sky-glow)"/>
    </linearGradient>
  </defs>
  <g role="img" aria-label="Photo of a steel building frame against a golden sunset sky">
    <rect width="848" height="484" fill="url(#photo-tone-a)"/>
    <rect width="848" height="484" fill="url(#photo-fade-a)"/>
  </g>
  <text class="brand-name" x="424" y="226" font-size="240" text-anchor="middle" textLength="430" lengthAdjust="spacingAndGlyphs">VLT</text>
  <text class="site-url" x="424" y="369" font-size="90" text-anchor="middle" textLength="676" lengthAdjust="spacingAndGlyphs">WWW.KR<tspan class="accent">VLT</tspan>.COM</text>
  <text class="service-line" x="136" y="450" font-size="50" textLength="240" lengthAdjust="spacingAndGlyphs">Temp Labor</text>
  <text class="service-line" x="406" y="450" font-size="50" textLength="304" lengthAdjust="spacingAndGlyphs">000-000-0000</text>
</svg>

<svg class="banner banner--warm" viewBox="0 0 848 484" aria-label="VLT temp labor banner, warm orange version">
  <defs>
    <linearGradient id="photo-fade-b" x1="0" y1="0" x2="0" y2="1">
      <stop offset="0" stop-color="var(--steel-amber)" stop-opacity="0"/>
      <stop offset="0.55" stop-color="#3a2410" stop-opacity="0.6"/>
      <stop offset="0.82" stop-color="#000" stop-opacity="1"/>
    </linearGradient>
    <linearGradient id="photo-tone-b" x1="0" y1="0" x2="1" y2="0">
      <stop offset="0" stop-color="#a8652a"/>
      <stop offset="0.55" stop-color="#c98a45"/>
      <stop offset="1" stop-color="var(--sky-glow)"/>
    </linearGradient>
  </defs>
  <g role="img" aria-label="Photo of a steel building frame against a golden sunset sky">
    <rect width="848" height="484" fill="url(#photo-tone-b)"/>
    <rect width="848" height="484" fill="url(#photo-fade-b)"/>
  </g>
  <text class="brand-name" x="424" y="226" font-size="240" text-anchor="middle" textLength="430" lengthAdjust="spacingAndGlyphs">VLT</text>
  <text class="site-url" x="424" y="369" font-size="90" text-anchor="middle" textLength="676" lengthAdjust="spacingAndGlyphs">WWW.KR<tspan class="accent">VLT</tspan>.COM</text>
  <text class="service-line" x="136" y="450" font-size="50" textLength="240" lengthAdjust="spacingAndGlyphs">Temp Labor</text>
  <text class="service-line" x="406" y="450" font-size="50" textLength="304" lengthAdjust="spacingAndGlyphs">000-000-0000</text>
</svg>

</body>
</html>
```